Frozen Yoghurt
Aufgabenstellung
Es soll eine Postkarte erstellt werden
auf die Vorteile des Produkts dargestellt werden
- kein fett (98% fettfrei)
- keine künstlichen süssungsmittel
- low calorien
- Viel Calcium
- Viel Eiweiss
- Vitamine durch Frucht topping
Die Postkarte soll gleichzeitig dazu dienen dass man sie mit zu uns ins Geschäft bringt und dann ein gratis Muster bekommt.
Mitbewerber: www.plumdrizzle.com, www.velvocup.com

```html
<!DOCTYPE html>
<html lang="de">
<head>
<meta charset="utf-8">
<title>Frozen Yoghurt – Postkarte</title>
<link rel="stylesheet" href="https://fonts.googleapis.com/css2?family=Open+Sans:ital,wght@0,400;0,600;0,700;1,400;1,700;1,800&display=swap">
<style>
  :root {
    --magenta: #c8104f;
    --magenta-dark: #9e0c3e;
    --sky: #2a9ad6;
    --sky-light: #d9eef9;
    --sky-mid: #a9d6f1;
    --ink: #3b3b3b;
    --rule: #9a9a9a;
    --paper: #ffffff;
    --frame: #d5d5d5;
  }
  * { box-sizing: border-box; margin: 0; padding: 0; }
  html, body { width: 850px; height: 1200px; overflow: hidden; background: var(--paper); }
  body { font-family: "Open Sans", Arial, sans-serif; position: relative; }

  .card { position: absolute; left: 14px; width: 822px; overflow: hidden; }

  /* Front */
  .card-front {
    top: 19px; height: 571px;
    background: radial-gradient(ellipse at 70% 20%, #f4fbff 0%, #cfe9f8 45%, #9dd0ee 100%);
  }
  .front-title {
    position: absolute; left: 74px; top: 48px;
    font-style: italic; font-weight: 800; font-size: 68px; line-height: 0.98;
    color: var(--paper);
    text-shadow: 2px 2px 0 var(--magenta), -1px -1px 0 var(--magenta), 1px -1px 0 var(--magenta), -1px 1px 0 var(--magenta), 4px 5px 0 var(--magenta-dark);
    transform: rotate(-5deg); transform-origin: left top;
  }
  .front-title .line-2 { display: block; padding-left: 18px; }
  .front-claim {
    position: absolute; left: 92px; top: 232px;
    font-style: italic; font-weight: 700; font-size: 25px; line-height: 1.3;
    color: var(--magenta);
    transform: rotate(-6deg); transform-origin: left top;
  }
  .front-photo { position: absolute; left: 400px; top: 160px; width: 430px; height: 420px; }
  .front-band { position: absolute; left: 0; bottom: 0; width: 822px; height: 200px; }
  .front-cta {
    position: absolute; left: 28px; top: 462px;
    font-weight: 700; font-size: 15px; color: var(--magenta);
    transform: rotate(11deg); transform-origin: left top;
  }
  .front-cta strong { font-weight: 800; }
  .butterfly { position: absolute; width: 34px; height: 26px; border-radius: 50%; background: rgba(255,255,255,0.9); }

  /* Back */
  .card-back {
    top: 607px; height: 577px;
    background: var(--paper); border: 1px solid var(--frame);
  }
  .back-wave { position: absolute; left: 0; bottom: 0; width: 822px; height: 200px; }
  .back-title {
    position: absolute; left: 68px; top: 62px;
    font-style: italic; font-weight: 800; font-size: 46px; line-height: 1.02;
    color: var(--magenta);
    transform: rotate(-5deg); transform-origin: left top;
  }
  .back-title .line-2 { display: block; }
  .back-butterfly { position: absolute; left: 340px; top: 180px; width: 30px; height: 24px; border-radius: 50%; background: var(--sky); }
  .benefits { position: absolute; left: 68px; top: 212px; width: 360px; color: var(--sky); }
  .benefits h2 { font-size: 19px; font-weight: 700; line-height: 1.25; margin-bottom: 20px; }
  .benefits ul { list-style: none; }
  .benefits li { position: relative; padding-left: 18px; font-size: 17.5px; line-height: 1.3; margin-bottom: 12px; }
  .benefits li::before {
    content: ""; position: absolute; left: 0; top: 9px;
    width: 8px; height: 8px; border: 1.5px solid var(--sky); border-radius: 50%;
  }
  .voucher { position: absolute; left: 68px; top: 470px; font-size: 16px; font-weight: 600; line-height: 1.35; color: var(--magenta); }
  .voucher strong { font-weight: 800; }
  .divider { position: absolute; left: 469px; top: 217px; width: 1px; height: 308px; background: var(--rule); }
  .brand-box {
    position: absolute; left: 597px; top: 41px; width: 166px; height: 94px;
    border: 2px solid var(--magenta); display: flex; align-items: center; justify-content: center; gap: 8px;
  }
  .brand-box .dot { width: 12px; height: 12px; border-radius: 50%; background: var(--magenta); }
  .brand-box .name { font-weight: 700; font-size: 17px; color: var(--magenta); }
  .visit { position: absolute; left: 488px; top: 285px; width: 282px; }
  .visit-lead { font-size: 16px; color: var(--sky); margin-bottom: 14px; }
  .visit-line {
    font-style: italic; font-size: 18px; color: var(--ink);
    border-bottom: 1px solid var(--rule); padding-bottom: 2px; margin-bottom: 14px;
  }
  .visit-close { font-weight: 700; font-size: 16px; color: var(--magenta); margin-top: 22px; }
</style>
</head>
<body>

<section class="card card-front">
  <div class="front-photo" role="img" aria-label="Frozen Yoghurt mit Müsli und Kirschen im Becher, umspült von Milchspritzern"
       style="background: radial-gradient(ellipse at 55% 50%, #fbf3e6 0%, #e9c9a0 28%, #b3263f 46%, rgba(255,255,255,0.7) 62%, rgba(255,255,255,0) 75%);"></div>
  <svg class="front-band" viewBox="0 0 822 200" preserveAspectRatio="none" aria-hidden="true">
    <path d="M0 70 C 220 110 420 170 822 150 L822 200 L0 200 Z" fill="#ffffff" opacity="0.85"/>
    <path d="M0 62 C 230 100 430 160 822 140 L822 158 C 430 180 220 124 0 86 Z" fill="var(--magenta)"/>
    <path d="M0 96 C 230 134 430 188 822 172 L822 200 L0 200 Z" fill="#d7edf9"/>
  </svg>
  <div class="front-cta">Mit dieser Karte <strong>JETZT GRATIS</strong> testen.</div>
  <div class="butterfly" role="img" aria-label="Schmetterling" style="left:750px; top:110px;"></div>
  <div class="butterfly" role="img" aria-label="Schmetterling" style="left:246px; top:458px;"></div>
  <div class="butterfly" role="img" aria-label="Schmetterling" style="left:322px; top:466px;"></div>
  <h1 class="front-title">Frozen <span class="line-2">Yoghurt</span></h1>
  <p class="front-claim">Locker Leichter Genuss<br>100% kalorienarm</p>
</section>

<section class="card card-back">
  <svg class="back-wave" viewBox="0 0 822 200" preserveAspectRatio="none" aria-hidden="true">
    <path d="M0 40 C 150 120 420 190 822 200 L0 200 Z" fill="var(--sky-light)"/>
    <path d="M0 90 C 180 160 420 195 700 200 L0 200 Z" fill="var(--sky-mid)" opacity="0.5"/>
  </svg>
  <h2 class="back-title">Frozen <span class="line-2">Yoghurt</span></h2>
  <div class="back-butterfly" role="img" aria-label="Schmetterling"></div>
  <div class="benefits">
    <h2>Der gesunde und leichte<br>Sommergenuss</h2>
    <ul>
      <li>nahezu fettrei - nur 2% Fett</li>
      <li>mit der extra Portion Eiweiß<br>und Calcium</li>
      <li>reich an Vitaminen durch eine<br>Vielzahl an Frucht-Toppings</li>
    </ul>
  </div>
  <p class="voucher"><strong>GUTSCHEIN</strong> einlösen und einen<br>Frozen Yoghurt <strong>GRATIS</strong> genießen.</p>
  <div class="divider"></div>
  <div class="brand-box"><span class="dot"></span><span class="name">Vital Corner</span></div>
  <div class="visit">
    <p class="visit-lead">Besuchen Sie uns in der...</p>
    <p class="visit-line">Linden Egge</p>
    <p class="visit-line">Cafebar Vital Corner</p>
    <p class="visit-line">Rosengasse 18-22</p>
    <p class="visit-line">3000 Bern</p>
    <p class="visit-close">Wir freuen uns auf Sie!</p>
  </div>
</section>

</body>
</html>
```